Poster & Banner for Outback tour company

Poster needed for tour company in the Australian outback. We will need it in an A2 format and if possible a larger banner format as Well please. It needs the Kestrel Tours logo but also the other logos (less obvious). It also needs to feature the Vantorix logo (uploaded).

The poster needs a list of the tours we offer as well as some of the pictures uploaded.

List of tours:

- Deluxe Tour of the Village and the Redspurs $99
- Marrandi Scenic Tour $85
- Starlight Redspurs Tour $60
- Quartz Trailside Tour $50

Industry/Entity Type

Tour Company

Font styles to use
Serif

Colors

Designer to choose colors to be used in the design.

Requirements
Must have
• Kestrel Tours logo/List of tours/

```html
<!DOCTYPE html>
<html lang="en">
<head>
<meta charset="utf-8">
<title>Kestrel Tours – List of the Tour</title>
<link href="https://fonts.googleapis.com/css2?family=Montserrat:wght@500;800&family=Noto+Serif:wght@600;700&display=swap" rel="stylesheet">
<style>
  :root{
    --page:#ececec;
    --red:#b3182b;
    --red-dark:#8e0f1f;
    --orange:#c97a2c;
    --teal:#3b7f97;
    --brown:#4a1611;
    --ink:#2b2422;
    --white:#ffffff;
    --badge:#34d39a;
  }
  *{box-sizing:border-box;margin:0;padding:0}
  html,body{width:1200px;height:2918px;overflow:hidden;background:var(--page)}
  .poster{
    position:absolute;left:40px;top:664px;width:1120px;height:1589px;
    overflow:hidden;font-family:"Montserrat",sans-serif;
    box-shadow:0 20px 50px rgba(0,0,0,.25);
  }
  .hero-photo{
    position:absolute;left:0;top:0;width:100%;height:760px;
    background:
      radial-gradient(ellipse 38% 60% at 50% 38%, #b9cfe0 0%, #c9d6df 40%, transparent 70%),
      linear-gradient(180deg,#9ebfdc 0%,#c8d5de 42%,#b58a6e 58%,#8e4a33 78%,#6f3322 100%);
  }
  .hero-photo::before,.hero-photo::after{
    content:"";position:absolute;top:0;height:100%;width:170px;
    background:linear-gradient(180deg,#8a4b33,#a0603f 50%,#6a3322);
  }
  .hero-photo::before{left:0;border-radius:0 0 60% 0}
  .hero-photo::after{right:0;width:140px;border-radius:0 0 0 60%}
  .lower-photo{
    position:absolute;left:0;top:740px;width:100%;height:849px;
    background:linear-gradient(180deg,#cfe6f3 0%,#a6cde4 30%,#7fb0cf 55%,#8a7a66 72%,#6e4a35 100%);
  }
  .brand{position:absolute;left:0;right:0;top:70px;text-align:center}
  .brand-mark{display:inline-block;width:60px;height:60px;background:var(--orange);border-radius:6px}
  .brand-name{
    margin-top:18px;font-family:"Noto Serif",serif;font-weight:700;
    font-size:50px;letter-spacing:-.5px;color:var(--ink);
  }
  .snapshots{position:absolute;left:0;top:660px;width:100%;height:290px}
  .snapshot{
    position:absolute;width:272px;height:222px;background:var(--white);padding:10px;
    box-shadow:0 6px 14px rgba(0,0,0,.3);
  }
  .snapshot .shot{width:100%;height:100%}
  .snapshot .pin{position:absolute;top:-12px;left:50%;width:16px;height:16px;border-radius:50%;background:#d4202e;margin-left:-8px}
  .s1{left:22px;top:40px;transform:rotate(-8deg)}
  .s1 .shot{background:linear-gradient(160deg,#d48a3c,#8a4a2a 60%,#5a3a2a)}
  .s2{left:290px;top:30px;transform:rotate(-4deg)}
  .s2 .shot{background:linear-gradient(180deg,#c9a27a,#7a4a30 60%,#5a2e1e)}
  .s3{left:560px;top:32px;transform:rotate(4deg)}
  .s3 .shot{background:linear-gradient(180deg,#c9b39c,#8a6a55 55%,#3e3028)}
  .s4{left:825px;top:26px;transform:rotate(11deg)}
  .s4 .shot{background:linear-gradient(180deg,#2a6fb3,#5a9ad0 40%,#d3934e 70%,#9a5a33)}
  .headline{position:absolute;left:0;right:0;top:955px;text-align:center}
  .headline-lead{font-weight:800;font-size:98px;line-height:1;color:var(--red);letter-spacing:-2px}
  .headline-tiles{display:flex;justify-content:center;gap:6px;margin-top:8px}
  .tile{
    width:114px;height:116px;border:5px solid var(--white);border-radius:12px;
    display:flex;align-items:center;justify-content:center;
    font-weight:800;font-size:96px;color:var(--white);
  }
  .tile.t1{background:var(--orange)}.tile.t2{background:var(--teal)}
  .tile.t3{background:var(--brown)}.tile.t4{background:var(--red)}
  .tour-list{position:absolute;left:87px;top:1192px;width:941px;display:flex}
  .tour{position:relative;flex:1;height:216px;padding-top:20px}
  .tour-body{height:196px;padding:100px 14px 0;text-align:center;color:var(--white);font-weight:500;font-size:23px;line-height:1.22}
  .tour.orange .tour-body{background:var(--orange)}
  .tour.teal .tour-body{background:var(--teal)}
  .tour.brown .tour-body{background:var(--brown)}
  .tour-price{
    position:absolute;left:10px;right:10px;top:0;height:100px;
    background:linear-gradient(180deg,var(--red),var(--red-dark));
    border-radius:10px 10px 50% 50% / 10px 10px 100% 100%;
    color:var(--white);font-weight:800;font-size:58px;text-align:center;line-height:92px;
  }
  .tour-price sup{font-size:28px;vertical-align:24px}
  .partners{
    position:absolute;left:119px;top:1408px;width:882px;height:141px;background:var(--white);
    border-radius:0 0 34px 34px;display:flex;align-items:center;justify-content:center;gap:22px;
    font-family:"Noto Serif",serif;font-weight:600;font-size:19px;line-height:1.2;color:var(--ink);
  }
  .partner{max-width:115px;text-align:center}
  .partner-divider{width:2px;height:70px;background:#333}
  .partner-award{display:flex;align-items:center;gap:10px}
  .partner-badge{width:70px;height:80px;background:var(--badge)}
</style>
</head>
<body>
  <main class="poster">
    <div class="hero-photo" role="img" aria-label="Four-wheel-drive tour bus parked on red desert ground, framed by a sandstone cave opening with a flat-topped mesa behind"></div>
    <div class="lower-photo" role="img" aria-label="Soft blurred outback landscape under a pale blue sky"></div>

    <header class="brand">
      <span class="brand-mark"></span>
      <div class="brand-name">Kestrel Tours</div>
    </header>

    <section class="snapshots">
      <figure class="snapshot s1"><span class="pin"></span><div class="shot" role="img" aria-label="Dugout homes carved into an orange rock hillside"></div></figure>
      <figure class="snapshot s2"><span class="pin"></span><div class="shot" role="img" aria-label="Underground church interior with arched stained-glass windows"></div></figure>
      <figure class="snapshot s3"><span class="pin"></span><div class="shot" role="img" aria-label="Two champagne glasses on stony ground at sunset"></div></figure>
      <figure class="snapshot s4"><span class="pin"></span><div class="shot" role="img" aria-label="Colourful desert hills under a deep blue sky"></div></figure>
    </section>

    <section class="headline">
      <h1 class="headline-lead">LIST OF THE</h1>
      <div class="headline-tiles">
        <span class="tile t1">T</span><span class="tile t2">O</span><span class="tile t3">U</span><span class="tile t4">R</span>
      </div>
    </section>

    <section class="tour-list">
      <article class="tour orange"><div class="tour-price"><sup>$</sup>99</div><p class="tour-body">Deluxe Tour of the Village and the Redspurs</p></article>
      <article class="tour teal"><div class="tour-price"><sup>$</sup>85</div><p class="tour-body">Marrandi Scenic Tour</p></article>
      <article class="tour brown"><div class="tour-price"><sup>$</sup>60</div><p class="tour-body">Starlight Redspurs Tour</p></article>
      <article class="tour orange"><div class="tour-price"><sup>$</sup>50</div><p class="tour-body">Quartz Trailside Tour</p></article>
    </section>

    <footer class="partners">
      <span class="partner">Ridgeline Resort</span>
      <span class="partner-divider"></span>
      <span class="partner">Campora Parks</span>
      <span class="partner-divider"></span>
      <span class="partner">Havenlea Villages</span>
      <span class="partner">Claybrick Motel</span>
      <span class="partner-award"><span class="partner-badge"></span><span class="partner">Vantorix</span></span>
    </footer>
  </main>
</body>
</html>
```